Web Design Project

we need to redesign our webpage. we would like a webpage that looks minimalist yet gives the company credibility. we are a office furniture retail store located at Porto Alegre, Brasil. it's a family-owned company and sell office chairs, furniture, blind, carpet, modular wall... we want to add also a online store in which products should sell for itself with big pictures, description, finishing options.
and maybe a channel where we could help architects to improve their projects with all our knoledge and products
the final design should communicate the store as a one-stop shop, a place that you find everything need for the office space.
our current webpage is www.lirantofurnis.com.br, but it doesn't have half of our products, and shows nothing of what we want.
Here in Brazil we don't use do have costumer reviews, so that is unnecessary...
Exemples of websites that shows a little of what we are looking for:
http://www.pelvican.com
http://www.tribuskadesk.com
http://www.zorvetaline.com

Target Market(s)

Everybody that either works, studies, owns a business, or have a computer at home.

Industry/Entity Type

Office Furniture

Requirements
Must have
• must have a architect and design banner in the homepage that leads to a design center page with technical informations

must have space for finishes and textile in each product

must havea ernonomic info banner in the homepage
Should not have
• A welcome photo and text in the homepage

```html
<!DOCTYPE html>
<html lang="pt-BR">
<head>
<meta charset="utf-8">
<title>Lirant Móveis para Escritório</title>
<link href="https://fonts.googleapis.com/css2?family=Ubuntu:wght@400;500;700&family=Raleway:wght@300;400&family=Lobster&display=swap" rel="stylesheet">
<style>
:root{
  --red:#e3161f;
  --ink:#555;
  --nav:#c6c6c6;
  --line:#e4e4e4;
  --frame:#e6e6e6;
  --band:#e5e5e5;
  --teal:#1c8b87;
  --amber:#f5a300;
  --sky:#27a3d8;
  --pink:#e5323f;
}
*{margin:0;padding:0;box-sizing:border-box}
html,body{width:844px;height:1200px;overflow:hidden;background:#fff}
body{position:relative;font-family:"Ubuntu",sans-serif;color:var(--ink)}
.abs{position:absolute}

.brand{left:98px;top:6px}
.brand-name{font-weight:700;font-size:40px;color:var(--red);line-height:42px;letter-spacing:-1px}
.brand-tag{font-size:7px;font-weight:700;color:#333;letter-spacing:.3px;border-top:1px solid #999;padding-top:2px;margin-left:12px;width:118px;text-align:right}
.top-phone{left:553px;top:8px;font-size:8px;color:var(--red);display:flex;align-items:center;gap:4px}
.top-shop{left:681px;top:8px;font-size:8px;color:#777;display:flex;align-items:center;gap:4px}
.search{left:622px;top:36px;width:118px;height:14px;border-radius:7px;background:#e8e8e8;font-size:7px;color:#888;padding:3px 8px;display:flex;justify-content:space-between;align-items:center}

.nav{left:98px;top:67px;width:648px;height:16px;display:flex;background:var(--nav)}
.nav a{font-size:7.5px;color:#fff;text-decoration:none;display:flex;align-items:center;justify-content:center;border-right:1px solid #fff;height:16px;letter-spacing:.2px}
.nav a.on{background:var(--red);font-weight:700}

.hero{left:98px;top:89px;width:648px;height:299px;background:linear-gradient(100deg,#f2f4f6 0%,#dfe5eb 40%,#cdd6df 65%,#eef1f4 100%);overflow:hidden}
.hero-photo{position:absolute;left:415px;top:15px;width:180px;height:280px;border-radius:40px 40px 20px 20px;background:linear-gradient(180deg,#3c56a6 0%,#2d4290 60%,#c9d0d8 80%,#e4e8ec 100%);opacity:.9}
.hero-title{position:absolute;left:19px;top:32px;font-family:"Raleway",sans-serif;font-weight:400;font-size:22px;color:#222;letter-spacing:.3px}
.hero-code{position:absolute;left:19px;top:58px;font-size:10px;color:#222}
.hero-script{position:absolute;left:26px;top:88px;font-family:"Lobster",cursive;font-size:42px;color:#111}
.hero-sub{position:absolute;left:90px;top:133px;font-family:"Raleway",sans-serif;font-weight:300;font-size:24px;color:#111}
.badge{position:absolute;left:27px;top:167px;width:82px;height:82px;border-radius:50%;background:var(--red);border:3px solid #f2dde0;color:#fff;font-size:7.5px;font-weight:700;text-align:center;line-height:10px;display:flex;align-items:center;justify-content:center;transform:rotate(-28deg)}
.dots{position:absolute;left:19px;top:269px;display:flex;gap:4px;align-items:center}
.dots span{width:7px;height:7px;background:#888}
.dots span.on{background:var(--red)}
.dots i{width:9px;height:9px;background:#fff;font-style:normal;font-size:7px;line-height:9px;text-align:center;color:#333}

.grid{left:98px;width:648px;height:250px;border-bottom:1px solid var(--line)}
.sep{position:absolute;top:0;width:1px;height:249px;background:var(--line)}
.card{position:absolute;top:0;width:105px;text-align:center}
.card-frame{width:105px;height:152px;border:5px solid var(--frame);background:#fff;display:flex;align-items:center;justify-content:center}
.card-img{width:78px;height:120px;border-radius:10px}
.card-title{font-size:11px;color:var(--red);margin-top:10px;white-space:nowrap;margin-left:-15px;margin-right:-15px}
.card-text{font-size:8px;line-height:11.5px;color:#666;margin:7px auto 0;width:90px}

.feat{top:948px;width:145px}
.feat-head{display:flex;align-items:center;gap:8px;height:28px}
.feat-ico{width:28px;height:28px;display:flex;align-items:center;justify-content:center}
.feat-title{font-size:11px;font-weight:700;line-height:11px}
.feat-text{font-size:8px;line-height:12.5px;color:#444;margin-top:10px}
.feat-link{font-size:8px;font-weight:700;color:#222;margin-top:12px}

.foot{left:98px;top:1103px;width:648px;height:61px;background:var(--band)}
.address{position:absolute;left:10px;top:8px;font-size:8.5px;line-height:14.5px;color:#888}
.news-title{position:absolute;left:364px;top:8px;font-size:10px;font-weight:700;color:var(--red)}
.news-text{position:absolute;left:364px;top:22px;font-size:7.5px;line-height:9.5px;color:#777;width:92px}
.field{position:absolute;left:467px;width:110px;height:17px;background:#fff;font-size:7.5px;color:#777;padding:4px 5px}
.submit{position:absolute;left:584px;top:9px;width:54px;height:42px;background:var(--red);color:#fff;font-size:7px;display:flex;align-items:center;justify-content:center}
.copy{left:98px;top:1174px;font-size:8.5px;color:#777}
.social{left:661px;top:1170px;display:flex;gap:4px}
.social span{width:18px;height:18px;border-radius:50%;background:#c9c9c9}
</style>
</head>
<body>

<header>
  <div class="abs brand">
    <div class="brand-name">Lirant</div>
    <div class="brand-tag">MÓVEIS PARA ESCRITÓRIO</div>
  </div>
  <div class="abs top-phone">
    <svg width="6" height="10" viewBox="0 0 6 10"><path d="M4 0 L1 2 Q0 5 1 8 L4 10 L5 8 L3 7 Q2 5 3 3 L5 2Z" fill="#e3161f"/></svg>
    (51) 3410.2875 / 3410.2890
  </div>
  <div class="abs top-shop">
    <svg width="10" height="9" viewBox="0 0 10 9"><path d="M0 1h2l1.5 5h5l1-3.5H3" fill="none" stroke="#888"/><circle cx="4" cy="8" r="1" fill="#888"/><circle cx="8" cy="8" r="1" fill="#888"/></svg>
    LOJA ON-LINE
  </div>
  <div class="abs search"><span>Pesquise aqui ...</span>
    <svg width="7" height="7" viewBox="0 0 7 7"><circle cx="3" cy="3" r="2" fill="none" stroke="#333"/><path d="M4.5 4.5 L6.5 6.5" stroke="#333"/></svg>
  </div>
  <nav class="abs nav">
    <a class="on" style="width:60px">INICIAL</a>
    <a style="width:60px">EMPRESA</a>
    <a style="width:68px">PRODUTOS</a>
    <a style="width:64px">SERVIÇOS</a>
    <a style="width:66px">PORTFÓLIO</a>
    <a style="width:74px">BIBLIOTECA</a>
    <a style="width:110px">SUGESTÕES DE LAYOUT</a>
    <a style="width:78px">ORÇAMENTO</a>
    <a style="width:68px;border-right:none">CONTATO</a>
  </nav>
</header>

<section class="abs hero">
  <div class="hero-photo" role="img" aria-label="Cadeira executiva de couro azul com base cromada"></div>
  <div class="hero-title">Varsen Super Premium e Premium</div>
  <div class="hero-code">037.06</div>
  <div class="hero-script">Sofisticado</div>
  <div class="hero-sub">Simplicidade</div>
  <div class="badge">EXPERIÊNCIA<br>UM NOVO NÍVEL<br>DE<br>CONFORTO</div>
  <div class="dots"><i>‹</i><span class="on"></span><span></span><span></span><span></span><span></span><i>›</i></div>
</section>

<section class="abs grid" style="top:405px">
  <div class="sep" style="left:120px"></div><div class="sep" style="left:254px"></div><div class="sep" style="left:390px"></div><div class="sep" style="left:526px"></div>
  <div class="card" style="left:0"><div class="card-frame"><div class="card-img" role="img" aria-label="Cadeira giratória azul" style="background:linear-gradient(#3a5ab0,#26408c)"></div></div>
    <div class="card-title">Call Center</div><div class="card-text">Voltada às empresas de teleatendimento / telemarketing nas modalidades...</div></div>
  <div class="card" style="left:136px"><div class="card-frame"><div class="card-img" role="img" aria-label="Cadeira de tela preta com assento verde-azulado" style="background:linear-gradient(#444 55%,#3a8f92 55%)"></div></div>
    <div class="card-title">Corvella</div><div class="card-text">Escolha, ajuste, viva a versatilidade de uma poltrona com seu estilo...</div></div>
  <div class="card" style="left:272px"><div class="card-frame"><div class="card-img" role="img" aria-label="Poltrona amarela com base cromada" style="background:linear-gradient(#dccf78,#c9b95a)"></div></div>
    <div class="card-title">Dorvi</div><div class="card-text">As formas arredonda-das garantem conforto e isenção de ruídos. Esta linha de...</div></div>
  <div class="card" style="left:407px"><div class="card-frame"><div class="card-img" role="img" aria-label="Cadeira giratória marrom" style="background:linear-gradient(#9a6048,#7a4a36)"></div></div>
    <div class="card-title">Estra</div><div class="card-text">Esta linha de poltronas possui os mais recentes conceitos de ergonomia...</div></div>
  <div class="card" style="left:543px"><div class="card-frame"><div class="card-img" role="img" aria-label="Poltronas de auditório vermelhas" style="background:linear-gradient(#d83a32,#b82424)"></div></div>
    <div class="card-title">Ovatio</div><div class="card-text">Para espaços amplos e completos...</div></div>
</section>

<section class="abs grid" style="top:672px">
  <div class="sep" style="left:120px"></div><div class="sep" style="left:254px"></div><div class="sep" style="left:390px"></div><div class="sep" style="left:526px"></div>
  <div class="card" style="left:0"><div class="card-frame"><div class="card-img" role="img" aria-label="Cadeira de tela preta com encosto de cabeça" style="background:linear-gradient(#3a3a3a,#1e1e1e)"></div></div>
    <div class="card-title">Flexmara</div><div class="card-text">Poltrona de linhas modernas e materiais recicláveis. Não utiliza madeira...</div></div>
  <div class="card" style="left:136px"><div class="card-frame"><div class="card-img" role="img" aria-label="Cadeira bege com encosto flexível" style="background:linear-gradient(#ddd6c4,#c8bfa8)"></div></div>
    <div class="card-title">Generis by Varnholt</div><div class="card-text">Produzida com materi-ais de alta performance e sustentáveis, a Generis ...</div></div>
  <div class="card" style="left:272px"><div class="card-frame"><div class="card-img" role="img" aria-label="Cadeira branca com assento verde" style="background:linear-gradient(#eeeeee 55%,#5a8f2a 55%)"></div></div>
    <div class="card-title">Verdant's</div><div class="card-text">Criada por Castori &amp; Mendel e inteiramente em material 100% reciclável...</div></div>
  <div class="card" style="left:407px"><div class="card-frame"><div class="card-img" role="img" aria-label="Poltrona executiva de couro preto" style="background:linear-gradient(#333,#151515)"></div></div>
    <div class="card-title">Ivra</div><div class="card-text">O design elegante, valorizado por linhas de costura acentuada, contornos...</div></div>
  <div class="card" style="left:543px"><div class="card-frame"><div class="card-img" role="img" aria-label="Estações de trabalho em escritório" style="background:linear-gradient(#d4d4d4,#7d7d7d);height:56px;width:92px;border-radius:4px"></div></div>
    <div class="card-title">Intera Work</div><div class="card-text">Em Melamínico 25 mm, acabamento em filete 2.5 mm todo o contorno...</div></div>
</section>

<section>
  <div class="abs feat" style="left:98px">
    <div class="feat-head"><div class="feat-ico" style="background:var(--pink)"><svg width="16" height="16" viewBox="0 0 16 16"><path d="M2 2L14 14M14 2L2 14" stroke="#fff" stroke-width="3"/></svg></div>
      <div class="feat-title" style="color:var(--pink)">ARCHITECTS</div></div>
    <div class="feat-text">Lorem Ipsum is simply dummy text of the printing and typesetting industry. Lorem Ipsum has been the industry's standard dummy text ever since the 1500s.</div>
    <div class="feat-link">Entrar ou Cadastre-se aqui <span style="color:var(--pink)">→</span></div>
  </div>
  <div class="abs feat" style="left:267px">
    <div class="feat-head"><div class="feat-ico" style="background:var(--teal)"><svg width="16" height="16" viewBox="0 0 16 16"><path d="M3 13L12 4l1 1-9 9z" fill="#fff"/></svg></div>
      <div class="feat-title" style="color:var(--teal)">Designer<br>Resource Center</div></div>
    <div class="feat-text">Lorem Ipsum is simply dummy text of the printing and typesetting industry. Lorem Ipsum has been the industry's standard dummy text ever since the 1500s.</div>
    <div class="feat-link">Entrar ou Cadastre-se aqui <span style="color:var(--teal)">→</span></div>
  </div>
  <div class="abs feat" style="left:436px">
    <div class="feat-head"><div class="feat-ico" style="background:var(--amber)"><svg width="12" height="16" viewBox="0 0 12 16"><rect x="1" y="1" width="10" height="14" rx="5" fill="none" stroke="#fff" stroke-width="1.5"/><path d="M6 1v5" stroke="#fff" stroke-width="1.5"/></svg></div>
      <div class="feat-title" style="color:var(--amber)">ERGO</div></div>
    <div class="feat-text">Lorem Ipsum is simply dummy text of the printing and typesetting industry. Lorem Ipsum has been the industry's standard dummy text ever since the 1500s.</div>
    <div class="feat-link">Entrar ou Cadastre-se aqui <span style="color:var(--amber)">→</span></div>
  </div>
  <div class="abs feat" style="left:603px">
    <div class="feat-head"><div class="feat-ico" style="background:var(--sky)"><svg width="16" height="16" viewBox="0 0 16 16"><path d="M8 2L14 5 8 8 2 5z" fill="#fff"/><path d="M2 8l6 3 6-3M2 11l6 3 6-3" fill="none" stroke="#fff" stroke-width="1.3"/></svg></div>
      <div class="feat-title" style="color:var(--sky)">FEATURE PRODUCT</div></div>
    <div class="feat-text">Lorem Ipsum is simply dummy text of the printing and typesetting industry. Lorem Ipsum has been the industry's standard dummy text ever since the 1500s.</div>
    <div class="feat-link">Entrar ou Cadastre-se aqui <span style="color:var(--sky)">→</span></div>
  </div>
</section>

<footer>
  <div class="abs foot">
    <div class="address">Rua Alvorada Serena, 512 - Jardim Auxiliadora,<br>Porto Alegre - RS<br>Tel.: (51) 3410.2875 / 3410.2890</div>
    <div class="news-title">NEWSLETTER</div>
    <div class="news-text">Cadastre-se abaixo para receber novidades para o seu escritório!</div>
    <div class="field" style="top:9px">Nome:</div>
    <div class="field" style="top:34px">Email:</div>
    <div class="submit">SUBMETER</div>
  </div>
  <div class="abs copy">© 2013 LirantMoveis. Todos os direitos reservados</div>
  <div class="abs social"><span></span><span></span><span></span><span></span></div>
</footer>

</body>
</html>
```